Emergency Vehicle Installer and Security Firm Needs a Business Card

Our company "Corvalt" need a business card for our Emergency Vehicle Equipment Installation and Infrastructure Security Business. We are contract designers, manufacturers and installers for Emergency Vehicle Fleets. This includes installation of Emergency Lights, Sirens, Vehicle Graphics and Radio Communications. We also supply this products to an international market. We also do consultant, and installation of high level security access, alarm and surveillance equipment for medium to large size businesses.

The design should represent a level of trust in our professionalism and expertise. It should visually display our ongoing relationship with the emergency services, but not overtake our commitment to high level security options.

Target Market(s)

Emergency Services and Businesses requiring high level security

Industry/Entity Type

Business

Contact Information for Business Card

*note complete details will be given to the winning designer for revising. The name "Mark Pell will be used to fill in name".

Mark Pell
Managing Director
Corvalt NZ Limited
Phone: +64 027 604 91352
Email: mark.pell@corvalt-example.co.nz

Requirements
Must have
• Card must be in black. Using our logo on the top as supplied. Designers should try having the reverse side as a blurred image of police lights (red and blue) with our logo in greyscale in the centre (this is not particularly a requirement, but feel free to play around with this option).
Nice to have
• A card design that looks good when spot UV printed. A clean compact and graphic design. A grey scale feel on the front (excluding logo, but you can play around with that idea). Rounded smooth text.
Should not have
• Will update this section as designs come through - feel free to submit what you feel would look good.

```html
<!DOCTYPE html>
<html lang="en">
<head>
<meta charset="utf-8">
<title>Corvalt Business Card</title>
<link href="https://fonts.googleapis.com/css2?family=Lato:wght@400;700;900&display=swap" rel="stylesheet">
<style>
  :root {
    --bg: #e9e6e2;
    --card-black: #050505;
    --brand-red: #ec2229;
    --white: #ffffff;
    --text-light: #f2f2f2;
  }
  * { box-sizing: border-box; margin: 0; padding: 0; }
  html, body {
    width: 1200px; height: 900px; overflow: hidden;
    background: var(--bg);
    font-family: "Lato", Arial, sans-serif;
  }
  .stage {
    width: 1200px; height: 900px;
    display: flex; align-items: center; justify-content: center; gap: 40px;
  }
  .card {
    position: relative;
    width: 540px; height: 310px;
    border-radius: 22px;
    overflow: hidden;
    box-shadow: 0 10px 26px rgba(0,0,0,.22);
  }

  /* Front */
  .card-front { background: var(--card-black); }
  .front-band {
    position: absolute; left: 0; bottom: 0; width: 100%; height: 24px;
  }
  .front-wordmark {
    position: absolute; left: 40px; top: 74px;
    font-weight: 900; font-size: 44px; letter-spacing: 1px;
    color: var(--white);
  }
  .front-divider {
    position: absolute; left: 250px; top: 44px;
    width: 30px; height: 210px;
  }
  .details {
    position: absolute; left: 282px; top: 50px;
    color: var(--text-light); font-size: 14px; line-height: 1.42;
  }
  .details .name {
    color: var(--brand-red); font-weight: 900; font-size: 22px; line-height: 1.2;
  }
  .details .role { font-size: 15px; }
  .details .line { display: flex; align-items: center; gap: 7px; white-space: nowrap; }
  .details .line svg { width: 13px; height: 13px; flex: none; }
  .details .address { margin-bottom: 2px; }

  /* Back */
  .card-back { background: var(--brand-red); }
  .back-wordmark {
    position: absolute; left: 0; right: 0; top: 112px;
    text-align: center;
    font-weight: 900; font-size: 64px; letter-spacing: 2px;
    color: var(--white);
  }
  .back-web {
    position: absolute; left: 92px; top: 208px;
    font-size: 13px; color: var(--white);
  }
</style>
</head>
<body>
<main class="stage">

  <section class="card card-front" aria-label="Card front">
    <svg class="front-band" viewBox="0 0 540 24" preserveAspectRatio="none" aria-hidden="true">
      <polygon points="0,0 320,0 300,24 0,24" fill="var(--brand-red)"/>
      <polygon points="332,0 540,0 540,24 312,24" fill="var(--white)"/>
    </svg>

    <div class="front-wordmark">CORVALT</div>

    <svg class="front-divider" viewBox="0 0 30 210" aria-hidden="true">
      <line x1="28" y1="0" x2="2" y2="210" stroke="var(--brand-red)" stroke-width="1.6"/>
    </svg>

    <div class="details">
      <div class="name">Mark Pell</div>
      <div class="role">Managing Director</div>
      <div class="address">2208 Harbour Rd<br>Napier, nz 4110</div>
      <div class="line">
        <svg viewBox="0 0 16 16" aria-hidden="true"><path d="M3.5 1.5l2.5 3-1.5 1.8c.8 1.8 2.2 3.2 4 4l1.8-1.5 3 2.5-1.6 2.2C7 13.5 2.5 9 1.5 3.1z" fill="var(--brand-red)"/></svg>
        <span>+64 027 604 91352</span>
      </div>
      <div class="line">
        <svg viewBox="0 0 16 16" aria-hidden="true"><rect x="1" y="3" width="14" height="10" fill="var(--brand-red)"/><path d="M1 3l7 6 7-6M1 13l5-5M15 13l-5-5" stroke="var(--card-black)" stroke-width="1.2" fill="none"/></svg>
        <span>mark.pell@corvalt-example.co.nz</span>
      </div>
      <div class="line">
        <svg viewBox="0 0 16 16" aria-hidden="true"><g fill="none" stroke="var(--brand-red)" stroke-width="1.3"><circle cx="8" cy="8" r="6.5"/><ellipse cx="8" cy="8" rx="3" ry="6.5"/><line x1="1.5" y1="8" x2="14.5" y2="8"/></g></svg>
        <span>www.corvalt-example.co.nz</span>
      </div>
    </div>
  </section>

  <section class="card card-back" aria-label="Card back">
    <div class="back-wordmark">CORVALT</div>
    <div class="back-web">www.corvalt-example.co.nz</div>
  </section>

</main>
</body>
</html>
```